Sports / Entertainment Media Co needs a biz card design

We are a media co / luxury lifestyle brand that targets professional athletes, entertainers and high net-worth fans. We are currently preparing for a relaunch and in need for new biz cards. I envision a black on black card with a pop of color on opposite side. Color Palette black, white, red etc. I want this card to exude sexiness and power. Very high stylized, hip and cool. I have attached the logo - I would like to see it all in black, but also open to other ideas. I will also upload a current card with all information needed on this new card. Furthermore I will add some samples of other cards I love. Thanks!!!

I provided suggestions, however I am open to all ideas!!   Be as creative as you can.  Think cutting-edge, sexy and powerful.  Take a look at the cards I uploaded to get a sense for what I like.  Thanks!!!

Entertainment

```html
<!DOCTYPE html>
<html lang="en">
<head>
<meta charset="utf-8">
<title>Stride Media Ventures – Business Card</title>
<link href="https://fonts.googleapis.com/css2?family=Open+Sans:wght@400;600;700&display=swap" rel="stylesheet">
<style>
  :root {
    --backdrop-center: #f4f4f6;
    --backdrop-edge: #8f9096;
    --front-paper: #e4e4df;
    --front-glow: #f6f6f3;
    --back-paper: #fbfbf3;
    --ink: #0d0d0d;
    --ink-soft: #6e7176;
    --accent: #e3141f;
  }
  * { margin: 0; padding: 0; box-sizing: border-box; }
  html, body { width: 1200px; height: 1200px; overflow: hidden; }
  body {
    position: relative;
    font-family: "Open Sans", Arial, sans-serif;
    background: radial-gradient(circle at 50% 48%, var(--backdrop-center) 0%, #d2d3d6 38%, var(--backdrop-edge) 100%);
  }
  .card { position: absolute; left: 228px; width: 744px; height: 424px; box-shadow: 0 2px 6px rgba(0,0,0,.12); }
  .card-front {
    top: 164px;
    border-radius: 0 34px 0 34px;
    background: radial-gradient(ellipse at 50% 52%, var(--front-glow) 0%, var(--front-paper) 70%, #d9d9d3 100%);
  }
  .front-band {
    position: absolute; left: 58px; right: 64px; top: 114px; height: 172px;
    background: linear-gradient(90deg, rgba(255,255,255,0), rgba(255,255,255,.35) 40%, rgba(255,255,255,.35) 60%, rgba(255,255,255,0));
  }
  .brand {
    position: absolute; display: flex; align-items: center; gap: 14px;
    font-weight: 700; color: var(--ink); letter-spacing: -4px; line-height: 1;
  }
  .brand-dot { display: block; border-radius: 50%; background: var(--accent); flex: none; }
  .card-front .brand { left: 72px; top: 120px; font-size: 148px; }
  .card-front .brand-dot { width: 40px; height: 40px; margin-top: 40px; }

  .card-back {
    top: 596px;
    border-radius: 34px 0 34px 0;
    background: linear-gradient(90deg, #f1f1e9 0%, var(--back-paper) 30%, var(--back-paper) 100%);
  }
  .card-back .brand {
    left: 80px; top: 52px; font-size: 64px; letter-spacing: -2px; gap: 10px;
    transform-origin: 0 0; transform: translate(80px, 0) rotate(90deg);
    left: 0; top: 52px;
  }
  .card-back .brand-dot { width: 18px; height: 18px; margin-top: 16px; }

  .person { position: absolute; left: 300px; width: 424px; top: 42px; text-align: center; }
  .person-name { font-size: 20px; font-weight: 700; color: var(--ink); letter-spacing: .3px; }
  .person-title { font-size: 19px; font-weight: 600; color: var(--ink-soft); margin-top: 1px; }
  .company { position: absolute; left: 268px; width: 488px; top: 164px; text-align: center; font-size: 25px; font-weight: 700; color: var(--ink); letter-spacing: .2px; }

  .contact-list { position: absolute; list-style: none; color: var(--ink-soft); font-size: 17px; line-height: 23.5px; }
  .contact-list li { display: flex; align-items: flex-start; gap: 10px; }
  .contact-list svg { width: 16px; height: 16px; flex: none; margin-top: 4px; fill: var(--accent); }
  .phones { left: 440px; top: 256px; }
  .details { left: 396px; top: 336px; }
  .details .indent { padding-left: 26px; }
</style>
</head>
<body>
  <section class="card card-front" aria-label="Card front">
    <div class="front-band"></div>
    <div class="brand"><span>stride</span><span class="brand-dot"></span></div>
  </section>

  <section class="card card-back" aria-label="Card back">
    <div class="brand"><span>stride</span><span class="brand-dot"></span></div>

    <div class="person">
      <p class="person-name">DANA MORROW</p>
      <p class="person-title">President</p>
    </div>
    <p class="company">STRIDE MEDIA VENTURES LLC</p>

    <ul class="contact-list phones">
      <li><svg viewBox="0 0 16 16" aria-hidden="true"><path d="M3 1.5l3 2.6-1.3 2.2c.9 2 2.6 3.7 4.6 4.6l2.2-1.3 2.6 3-1.6 1.9C7 14.3 1.7 9 1.1 3.1z"/></svg>305 555 0148</li>
      <li><svg viewBox="0 0 16 16" aria-hidden="true"><path d="M5 1h6a1 1 0 0 1 1 1v12a1 1 0 0 1-1 1H5a1 1 0 0 1-1-1V2a1 1 0 0 1 1-1zm1 2v7h4V3zm2 9a1 1 0 1 0 0 2 1 1 0 0 0 0-2z"/></svg>954 555 0192</li>
      <li><svg viewBox="0 0 16 16" aria-hidden="true"><path d="M4 1h7l1 2v3h2v8H2V6h2zm1 1v4h6V3.5L10.4 2zM4 9v1h2V9zm3 0v1h2V9zm3 0v1h2V9zm-6 2v1h2v-1zm3 0v1h2v-1zm3 0v1h2v-1z"/></svg>305 555 0176</li>
    </ul>

    <ul class="contact-list details">
      <li><svg viewBox="0 0 16 16" aria-hidden="true"><path d="M1 3h14v1.2L8 8.6 1 4.2zm0 2.6l7 4.4 7-4.4V13H1z"/></svg>dana@stridemedia.com</li>
      <li><svg viewBox="0 0 16 16" aria-hidden="true"><path d="M8 1.5l7 6-1 1.1-1-.9V14H9.5v-4h-3v4H3V7.7l-1 .9-1-1.1z"/></svg>4420 NE 12th Avenue, Ste 300</li>
      <li class="indent">Miami, FL 33137</li>
    </ul>
  </section>
</body>
</html>
```